Need help in designing new business card utilizing our new logo.

BuildMarq Solutions works with Construction Business Owners, Managers & IT Professionals to strengthen software usage and increase user productivity.

Our Construction Accounting and Mobile Field Management Software Clients engage with us in the following areas:

New Software Implementations
Software Re-Implementations
Redesigning Software Usage at the User Level
Project Coordination & Management
Continued Software Support

Old tag line:
Planning Clearly - Delivering Better Results

www.buildmarq-solutions.example

Stride 4 is a product, but not needed for a new business card.

```html
<!DOCTYPE html>
<html lang="en">
<head>
<meta charset="utf-8">
<title>BuildMarq Solutions – Business Card</title>
<link href="https://fonts.googleapis.com/css2?family=Open+Sans:wght@400;600&family=Oswald:wght@400;500&display=swap" rel="stylesheet">
<style>
  :root{
    --bg:#2a2a2c;
    --card-dark:#1b1b1d;
    --purple:#4b3fa8;
    --purple-light:#7068c4;
    --grey-band:#c8c8cc;
    --paper:#f7f7fa;
    --ink:#1e1e22;
    --white:#ffffff;
  }
  *{box-sizing:border-box;margin:0;padding:0}
  html,body{width:1200px;height:800px;overflow:hidden;background:var(--bg);font-family:"Open Sans",sans-serif}
  .stage{width:1200px;height:800px;display:flex;align-items:center;justify-content:center;gap:40px}
  .card{width:560px;height:320px;border-radius:18px;overflow:hidden;position:relative;flex:none}

  /* front */
  .card-front{background:var(--card-dark);display:flex;flex-direction:column;align-items:center;justify-content:center;gap:22px}
  .front-brand{display:flex;align-items:center;gap:14px}
  .brand-mark{width:38px;height:38px;background:var(--purple);flex:none}
  .brand-name{font-family:"Open Sans",sans-serif;font-weight:600;font-size:38px;color:var(--purple-light);letter-spacing:.5px;white-space:nowrap}
  .tagline{font-size:17px;color:var(--purple-light);white-space:nowrap}

  /* back */
  .card-back{background:var(--paper)}
  .back-brand{position:absolute;top:26px;right:28px;background:var(--white);padding:16px 22px;display:flex;align-items:center;gap:10px}
  .back-brand .brand-mark{width:22px;height:22px}
  .back-brand .brand-name{font-size:22px;color:var(--purple)}
  .person{position:absolute;left:36px;top:118px}
  .person-name{font-family:"Oswald",sans-serif;font-weight:500;font-size:30px;color:var(--ink);letter-spacing:.5px;line-height:1.3}
  .person-title{font-family:"Oswald",sans-serif;font-size:17px;color:var(--purple);line-height:1.3}
  .band-services{position:absolute;left:0;top:190px;width:480px;height:24px;background:var(--grey-band);clip-path:polygon(0 0,94% 0,100% 100%,0 100%);font-size:12px;color:var(--purple);padding:4px 0 0 36px;white-space:nowrap}
  .band-address{position:absolute;left:0;top:214px;width:560px;height:26px;background:var(--purple);font-size:12px;color:var(--white);display:flex;align-items:center;gap:10px;padding-left:20px;white-space:nowrap}
  .contact{position:absolute;left:0;top:240px;width:560px;height:80px;background:var(--card-dark);display:flex;justify-content:space-between;padding:14px 24px 0 20px}
  .contact ul{list-style:none;display:flex;flex-direction:column;gap:10px}
  .contact li{display:flex;align-items:center;gap:10px;font-size:12.5px;color:var(--white);white-space:nowrap}
  .contact-web li{flex-direction:row-reverse}
  .icon{width:18px;height:18px;background:var(--purple);border-radius:3px;display:flex;align-items:center;justify-content:center;flex:none}
  .icon svg{width:12px;height:12px;fill:none;stroke:var(--white);stroke-width:2}
  .pin svg{width:14px;height:14px;display:block}
</style>
</head>
<body>
<main class="stage">
  <section class="card card-front">
    <div class="front-brand">
      <span class="brand-mark"></span>
      <span class="brand-name">BuildMarq Solutions</span>
    </div>
    <p class="tagline">Planning Clearly - Delivering Better Results</p>
  </section>

  <section class="card card-back">
    <div class="back-brand">
      <span class="brand-mark"></span>
      <span class="brand-name">BuildMarq Solutions</span>
    </div>
    <div class="person">
      <p class="person-name">DANA R. WHITLOW</p>
      <p class="person-title">OWNER</p>
    </div>
    <div class="band-services">Consulting Accounting Software Consultants</div>
    <div class="band-address">
      <span class="pin"><svg viewBox="0 0 24 24"><path d="M12 22s7-7 7-12a7 7 0 0 0-14 0c0 5 7 12 7 12z" fill="#fff" stroke="none"/><circle cx="12" cy="10" r="2.5" fill="#4b3fa8" stroke="none"/></svg></span>
      14B Harbor Lane - PMB 118, Millbrook Falls NY 12000
    </div>
    <div class="contact">
      <ul class="contact-phone">
        <li><span class="icon"><svg viewBox="0 0 24 24"><path d="M5 3h4l2 5-3 2a11 11 0 0 0 6 6l2-3 5 2v4a2 2 0 0 1-2 2A17 17 0 0 1 3 5a2 2 0 0 1 2-2z"/></svg></span>800-555-0142 ext.100</li>
        <li><span class="icon"><svg viewBox="0 0 24 24"><rect x="6" y="3" width="12" height="18" rx="2"/></svg></span>518-555-0187</li>
      </ul>
      <ul class="contact-web">
        <li><span class="icon"><svg viewBox="0 0 24 24"><circle cx="12" cy="12" r="9"/><path d="M3 12h18M12 3c3 3 3 15 0 18M12 3c-3 3-3 15 0 18"/></svg></span>www.buildmarq-solutions.example</li>
        <li><span class="icon"><svg viewBox="0 0 24 24"><rect x="3" y="6" width="18" height="12"/><path d="M3 6l9 7 9-7"/></svg></span>dana.whitlow@buildmarq-solutions.example</li>
      </ul>
    </div>
  </section>
</main>
</body>
</html>
```